" É uma pequena fábrica com injetoras plásticas, e a produção poderá ser a mais variada possível. Podemos, por exemplo, criar desde utensílios plásticos (cabide, potes, baldes), brinquedos e, até mesmo, peças para indústrias. Temos também a parte de reciclagem, onde tratamos o plástico desde o lixo até a produção destes itens. No meu ponto de vista deve ser algo genérico, que demonstre criação, inovação, transformação, visão de futuro. "

```html
<!DOCTYPE html>
<html lang="pt-BR">
<head>
<meta charset="UTF-8">
<title>Moldava – Cartão de Visita</title>
<link href="https://fonts.googleapis.com/css2?family=Montserrat:wght@700&family=Roboto:wght@400&display=swap" rel="stylesheet">
<style>
  :root {
    --navy: #0f2a56;
    --orange: #f57c14;
    --white: #ffffff;
    --ink: #2c3340;
    --backdrop: #e9e6e1;
  }
  * { margin: 0; padding: 0; box-sizing: border-box; }
  html, body { width: 1200px; height: 1200px; overflow: hidden; }
  body {
    background: var(--backdrop);
    position: relative;
    font-family: 'Roboto', Arial, sans-serif;
  }
  .card {
    position: absolute;
    left: 230px;
    width: 740px;
    height: 350px;
    overflow: hidden;
    box-shadow: 0 8px 24px rgba(0,0,0,0.25);
  }
  .card-front { top: 170px; background: var(--navy); }
  .card-back { top: 600px; background: var(--navy); }
  .card svg.shapes { position: absolute; inset: 0; }

  .brand {
    position: absolute;
    display: flex;
    align-items: center;
    font-family: 'Montserrat', Arial, sans-serif;
    font-weight: 700;
    color: var(--white);
    letter-spacing: 2px;
  }
  .brand-mark { background: var(--orange); display: inline-block; }
  .front-brand { left: 0; right: 0; top: 120px; justify-content: center; font-size: 64px; gap: 18px; }
  .front-brand .brand-mark { width: 34px; height: 34px; }

  .back-brand { left: 40px; top: 84px; flex-direction: column; align-items: flex-start; }
  .back-brand .brand-row { display: flex; align-items: center; gap: 10px; font-size: 28px; }
  .back-brand .brand-mark { width: 18px; height: 18px; }
  .back-brand .brand-tagline {
    font-size: 10px; letter-spacing: 3px; color: var(--orange);
    margin-left: 28px; margin-top: 2px; font-weight: 700;
  }

  .contact { position: absolute; left: 362px; top: 72px; list-style: none; color: var(--ink); font-size: 23px; line-height: 1.3; }
  .contact li { display: flex; align-items: flex-start; gap: 12px; margin-bottom: 8px; }
  .contact .icon { width: 26px; height: 26px; flex: none; margin-top: 2px; }
  .contact .lines { display: flex; flex-direction: column; }

  .corner-brand {
    position: absolute; right: 24px; bottom: 22px;
    font-family: 'Montserrat', Arial, sans-serif; font-weight: 700;
    font-size: 24px; color: var(--white); letter-spacing: 2px;
  }
</style>
</head>
<body>

<section class="card card-front">
  <svg class="shapes" width="740" height="350" viewBox="0 0 740 350">
    <polygon class="stand-band" points="175,286 571,286 595,350 139,350" fill="var(--orange)"/>
  </svg>
  <div class="brand front-brand"><span class="brand-mark"></span>MOLDAVA</div>
</section>

<section class="card card-back">
  <svg class="shapes" width="740" height="350" viewBox="0 0 740 350">
    <path class="accent-curve" d="M318,0 Q250,170 214,350 L236,350 Q268,170 336,0 Z" fill="var(--orange)"/>
    <path class="info-panel" d="M336,0 L740,0 L740,350 L236,350 Q268,170 336,0 Z" fill="var(--white)"/>
    <path class="corner-band" d="M440,350 Q540,250 740,225 L740,350 Z" fill="var(--navy)"/>
    <path class="corner-accent" d="M680,180 L740,150 L740,198 L690,216 Z" fill="var(--orange)"/>
  </svg>

  <div class="brand back-brand">
    <div class="brand-row"><span class="brand-mark"></span>MOLDAVA</div>
    <div class="brand-tagline">INJEÇÃO PLÁSTICA</div>
  </div>

  <ul class="contact">
    <li>
      <svg class="icon" viewBox="0 0 26 26"><circle cx="13" cy="13" r="13" fill="var(--orange)"/><circle cx="13" cy="13" r="7" fill="none" stroke="#fff" stroke-width="1.6"/><path d="M6 13h14M13 6v14" stroke="#fff" stroke-width="1.4"/></svg>
      <span class="lines"><span>Endereço</span><span>Cidade - Estado</span><span>www.site.com</span></span>
    </li>
    <li>
      <svg class="icon" viewBox="0 0 26 26"><circle cx="13" cy="13" r="13" fill="var(--orange)"/><rect x="7" y="8.5" width="12" height="9" fill="none" stroke="#fff" stroke-width="1.6"/><path d="M7 9l6 5 6-5" fill="none" stroke="#fff" stroke-width="1.4"/></svg>
      <span>email@email.com</span>
    </li>
    <li>
      <svg class="icon" viewBox="0 0 26 26"><circle cx="13" cy="13" r="13" fill="var(--orange)"/><path d="M9 7c1 0 2 2.5 2 3s-1 1-1 1.6c.5 1.6 2 3 3.4 3.4.6 0 1-1 1.6-1s3 1 3 2c0 1.5-1.5 2.5-3 2.2C11 17.5 8.5 15 7.8 11 7.5 9 8 7 9 7z" fill="#fff"/></svg>
      <span>11- 12345-6789</span>
    </li>
  </ul>

  <div class="corner-brand">MOLDAVA</div>
</section>

</body>
</html>
```